Events & Entertainment Production Coordination Business Cards

We need a business card for a new company based in Los Angeles called "Bright Stage Works"
Our company brings people together for events and helps coordinate different productions. We bring artists from a different country to perform or do events in the U.S.
We are looking for something fun, lively, colorful, creative, and simple.
Nothing that looks too crisp, dark, stiff, or modern.
We connect people from different parts of the world, so definitely something eye-catching will be great!
Colors we would like to see are Black, Yellow, Red, White, Brown to name a few. (Feel free to use more!)
(Double-sided is an option also)
Industry/Entity Type
Business
Contact Information for Business Card
Contact Information to put on Business Card:
Name
Title
Address - 2 lines
Phone - place for 3 numbers
E-mail
URL
Look and feel

```html
<!DOCTYPE html>
<html lang="en">
<head>
<meta charset="utf-8">
<title>Bright Stage Works – Business Card</title>
<link rel="stylesheet" href="https://fonts.googleapis.com/css2?family=Montserrat:wght@700;800&family=Open+Sans:wght@400;600&display=swap">
<style>
  :root {
    --ink: #111111;
    --brand-red: #e8202a;
    --paper: #ffffff;
    --backdrop: #e9e4de;
    --card-shadow: rgba(0, 0, 0, 0.18);
  }
  * { margin: 0; padding: 0; box-sizing: border-box; }
  html, body {
    width: 1200px;
    height: 902px;
    overflow: hidden;
    background: var(--backdrop);
  }
  .stage {
    position: relative;
    width: 1200px;
    height: 902px;
  }
  .business-card {
    position: absolute;
    left: 100px;
    top: 165px;
    width: 1000px;
    height: 572px;
    background: var(--paper);
    box-shadow: 0 10px 30px var(--card-shadow);
    overflow: hidden;
    font-family: "Open Sans", Arial, sans-serif;
    color: var(--ink);
  }
  .card-swoosh {
    position: absolute;
    inset: 0;
    width: 1000px;
    height: 572px;
  }
  .brand-name {
    position: absolute;
    left: 50px;
    top: 58px;
    font-family: "Montserrat", Arial, sans-serif;
    font-weight: 800;
    font-size: 70px;
    line-height: 80px;
    letter-spacing: 1px;
    color: var(--ink);
    text-transform: uppercase;
  }
  .brand-name .brand-dot {
    display: inline-block;
    width: 44px;
    height: 44px;
    margin-left: 18px;
    border-radius: 50%;
    background: var(--brand-red);
    vertical-align: 2px;
  }
  .person {
    position: absolute;
    left: 50px;
    top: 283px;
    display: flex;
    align-items: baseline;
    white-space: nowrap;
  }
  .person-name {
    font-family: "Montserrat", Arial, sans-serif;
    font-weight: 800;
    font-size: 31px;
    letter-spacing: -0.3px;
  }
  .person-title {
    margin-left: 12px;
    padding-left: 10px;
    border-left: 2px solid var(--brand-red);
    font-size: 27px;
    color: var(--brand-red);
    line-height: 30px;
  }
  .contact-list {
    position: absolute;
    left: 50px;
    top: 372px;
    list-style: none;
  }
  .contact-item {
    display: flex;
    align-items: center;
    height: 31px;
    font-size: 27px;
    line-height: 31px;
  }
  .contact-icon {
    width: 24px;
    height: 24px;
    margin-right: 6px;
    flex-shrink: 0;
  }
  .website {
    position: absolute;
    left: 50px;
    top: 494px;
    font-size: 26px;
    font-weight: 600;
    color: var(--brand-red);
  }
  .address {
    position: absolute;
    left: 488px;
    top: 470px;
    width: 282px;
    font-size: 27px;
    line-height: 34px;
    text-align: right;
    font-style: normal;
  }
</style>
</head>
<body>
<main class="stage">
  <article class="business-card">
    <svg class="card-swoosh" viewBox="0 0 1000 572" aria-hidden="true">
      <rect width="1000" height="572" fill="var(--ink)"/>
      <path d="M625,0 C820,60 930,200 908,340 C892,440 805,525 735,572 L0,572 L0,0 Z" fill="var(--paper)"/>
      <path d="M320,0 L470,0 C700,40 880,180 888,360 C892,460 825,530 772,572 L760,572 C815,525 868,455 864,360 C852,215 690,70 320,0 Z" fill="var(--brand-red)"/>
      <path d="M830,520 C800,545 780,560 760,572 L765,572 C790,558 812,542 830,520 Z" fill="var(--brand-red)"/>
    </svg>

    <h1 class="brand-name">Bright Stage<br>Works<span class="brand-dot"></span></h1>

    <p class="person">
      <span class="person-name">EMPLOYEE NAME</span>
      <span class="person-title">Managing Director</span>
    </p>

    <ul class="contact-list">
      <li class="contact-item">
        <svg class="contact-icon" viewBox="0 0 24 24" aria-hidden="true"><rect width="24" height="24" fill="var(--brand-red)"/><rect x="7" y="3" width="10" height="18" rx="1.5" fill="none" stroke="#fff" stroke-width="1.8"/><rect x="9" y="6" width="6" height="5" fill="#fff"/></svg>
        123-456-7890
      </li>
      <li class="contact-item">
        <svg class="contact-icon" viewBox="0 0 24 24" aria-hidden="true"><rect width="24" height="24" fill="var(--brand-red)"/><path d="M4,9 C4,5 20,5 20,9 L17,10 L16,8 L8,8 L7,10 Z" fill="#fff"/><rect x="6" y="12" width="12" height="7" rx="1" fill="#fff"/></svg>
        123-456-7890
      </li>
      <li class="contact-item">
        <svg class="contact-icon" viewBox="0 0 24 24" aria-hidden="true"><rect width="24" height="24" fill="var(--brand-red)"/><rect x="7" y="3" width="10" height="6" fill="#fff"/><rect x="4" y="10" width="16" height="7" rx="1" fill="#fff"/><rect x="7" y="15" width="10" height="6" fill="#fff" stroke="var(--brand-red)" stroke-width="1"/></svg>
        123-456-7890
      </li>
      <li class="contact-item">
        <svg class="contact-icon" viewBox="0 0 24 24" aria-hidden="true"><rect width="24" height="24" fill="var(--brand-red)"/><rect x="4" y="6" width="16" height="12" fill="none" stroke="#fff" stroke-width="1.8"/><path d="M4,6 L12,13 L20,6" fill="none" stroke="#fff" stroke-width="1.8"/></svg>
        company@yourmail.com
      </li>
    </ul>

    <p class="website">www.yourwebsite.com</p>

    <address class="address">your address Avenue<br>Brightvale, CA 0000</address>
  </article>
</main>
</body>
</html>
```